Private Learning Centre in Singapore needs a flyer design

We need a flyer design for our upcoming education fair and also able to use it for day to day purpose. The aim is to attract parents, students to enrol for classes by offering them free trial class/assessment. 2 sided flyer with the front page as the logo only and details on the other page. We would like to see a final design in blue, white and it should be curious and attractive enough not to allow customers to throw it away once they received it.

Education

```html
<!DOCTYPE html>
<html lang="en">
<head>
<meta charset="utf-8">
<title>Bright Path Academy – Flyer</title>
<link href="https://fonts.googleapis.com/css2?family=Open+Sans:wght@400;600;700;800&display=swap" rel="stylesheet">
<style>
  :root {
    --stage: #151617;
    --deep-blue: #1f6f9e;
    --mid-blue: #2c8ac0;
    --sky-blue: #5ab3dc;
    --pale-blue: #d9eef9;
    --white: #ffffff;
    --ink: #1b4f72;
  }
  * { box-sizing: border-box; margin: 0; padding: 0; }
  html, body {
    width: 1200px; height: 1000px; overflow: hidden;
    background: var(--stage);
    font-family: "Open Sans", Arial, sans-serif;
  }
  .flyer {
    position: absolute; top: 200px;
    width: 390px; height: 600px;
    overflow: hidden;
    box-shadow: 0 18px 40px rgba(0,0,0,.6);
  }
  .flyer--front { left: 180px; }
  .flyer--back { left: 630px; }
  .flyer svg.backdrop { position: absolute; inset: 0; }

  /* front */
  .brand-lockup {
    position: absolute; top: 190px; left: 0; width: 100%;
    display: flex; align-items: center; justify-content: center; gap: 10px;
  }
  .brand-lockup__dot {
    width: 22px; height: 22px; border-radius: 50%; background: var(--deep-blue);
  }
  .brand-lockup__name {
    font-weight: 700; font-size: 23px; letter-spacing: 1px; color: var(--deep-blue);
  }

  /* back */
  .offer-ribbon {
    position: absolute; top: 40px; left: 45px; width: 300px; height: 90px;
  }
  .offer-ribbon__title {
    position: absolute; top: 14px; left: 0; width: 100%; text-align: center;
    font-weight: 800; font-size: 25px; line-height: 30px; color: var(--white);
    text-shadow: 0 2px 3px rgba(0,0,0,.35);
  }
  .about-panel {
    position: absolute; top: 200px; left: 28px; width: 334px; height: 150px;
  }
  .about-panel__shadow {
    position: absolute; inset: 8px -4px -10px 6px;
    background: var(--deep-blue); transform: rotate(-3deg);
  }
  .about-panel__card {
    position: absolute; inset: 0;
    background: linear-gradient(180deg, #7cc6e8, var(--sky-blue));
    box-shadow: 0 4px 10px rgba(0,0,0,.3);
    padding: 20px 20px;
  }
  .about-panel__text {
    color: var(--white); font-size: 13px; line-height: 1.42; font-weight: 600;
    text-align: center; text-shadow: 0 1px 2px rgba(0,0,0,.3);
  }
  .contact {
    position: absolute; left: 28px; top: 478px;
    color: var(--ink); font-size: 11.5px;
  }
  .contact__name { font-weight: 700; font-size: 16px; color: var(--mid-blue); margin-bottom: 6px; }
  .contact__row { display: flex; align-items: center; gap: 8px; margin-bottom: 3px; }
  .contact__icon { width: 11px; height: 11px; flex: none; }
  .footer-brand {
    position: absolute; right: 22px; top: 410px;
    display: flex; align-items: center; gap: 6px;
  }
  .footer-brand__dot { width: 14px; height: 14px; border-radius: 50%; background: var(--deep-blue); }
  .footer-brand__name { font-weight: 700; font-size: 12px; color: var(--deep-blue); }
</style>
</head>
<body>

<section class="flyer flyer--front">
  <svg class="backdrop" width="390" height="600" viewBox="0 0 390 600">
    <defs>
      <radialGradient id="front-glow" cx="50%" cy="42%" r="70%">
        <stop offset="0" stop-color="#ffffff"/>
        <stop offset=".45" stop-color="#bfe2f4"/>
        <stop offset="1" stop-color="#2c8ac0"/>
      </radialGradient>
      <linearGradient id="photo-area" x1="0" y1="0" x2="0" y2="1">
        <stop offset="0" stop-color="#d9eef9" stop-opacity="0"/>
        <stop offset="1" stop-color="#8cc6e6"/>
      </linearGradient>
    </defs>
    <rect width="390" height="600" fill="url(#front-glow)"/>
    <path d="M0 0H390V38L195 72L0 38Z" fill="#2a7fb0"/>
    <polyline points="0,48 195,82 390,48" fill="none" stroke="#fff" stroke-width="6"/>
    <rect role="img" aria-label="Photo placeholder: open meadow with a lone tree under a blue sky" x="0" y="380" width="390" height="150" fill="url(#photo-area)"/>
    <path d="M0 525L200 470L390 525V600H0Z" fill="#1f6f9e"/>
    <polyline points="0,515 200,460 390,515" fill="none" stroke="#fff" stroke-width="7"/>
  </svg>
  <div class="brand-lockup">
    <span class="brand-lockup__dot"></span>
    <span class="brand-lockup__name">BRIGHT PATH ACADEMY</span>
  </div>
</section>

<section class="flyer flyer--back">
  <svg class="backdrop" width="390" height="600" viewBox="0 0 390 600">
    <defs>
      <radialGradient id="back-glow" cx="50%" cy="35%" r="75%">
        <stop offset="0" stop-color="#8fd0ee"/>
        <stop offset="1" stop-color="#2c8ac0"/>
      </radialGradient>
    </defs>
    <rect width="390" height="600" fill="url(#back-glow)"/>
    <path d="M0 455Q200 470 390 380V600H0Z" fill="#fff"/>
  </svg>

  <div class="offer-ribbon">
    <svg width="300" height="90" viewBox="0 0 300 90">
      <path d="M30 50H270L240 85H60Z" fill="#2a7fb0" stroke="#fff" stroke-width="2"/>
      <path d="M10 10H290L280 30L290 50H10L20 30Z" fill="#1f6f9e"/>
    </svg>
    <div class="offer-ribbon__title">Free Trail Class</div>
  </div>

  <div class="about-panel">
    <div class="about-panel__shadow"></div>
    <div class="about-panel__card">
      <p class="about-panel__text">Bright Path Academy is where you can develop academic and life skills. Our teachers are the heartbeat of the business. They inspire and nurture students, helping them surpass their expectations. We cover English, Mathematics and Science from Primary and Secondary Levels.</p>
    </div>
  </div>

  <div class="footer-brand">
    <span class="footer-brand__dot"></span>
    <span class="footer-brand__name">BRIGHT PATH ACADEMY</span>
  </div>

  <div class="contact">
    <p class="contact__name">Bright Path Academy</p>
    <p class="contact__row">
      <svg class="contact__icon" viewBox="0 0 12 12"><path d="M6 0a4 4 0 0 0-4 4c0 3 4 8 4 8s4-5 4-8a4 4 0 0 0-4-4zm0 5.5A1.5 1.5 0 1 1 6 2.5a1.5 1.5 0 0 1 0 3z" fill="#1f6f9e"/></svg>
      18 Harbour View Road S400123
    </p>
    <p class="contact__row">
      <svg class="contact__icon" viewBox="0 0 12 12"><path d="M2.5 0.5l2 2.5-1.2 1.3a7 7 0 0 0 4.4 4.4L9 7.5l2.5 2-1.2 2C5 11.5 0.5 7 0.5 1.7z" fill="#1f6f9e"/></svg>
      6123 4567
    </p>
    <p class="contact__row">
      <svg class="contact__icon" viewBox="0 0 12 12"><rect x="0.5" y="2" width="11" height="8" fill="#1f6f9e"/><polyline points="0.5,2 6,6.5 11.5,2" fill="none" stroke="#fff" stroke-width="1"/></svg>
      hello@brightpathacademy.com
    </p>
    <p class="contact__row">
      <svg class="contact__icon" viewBox="0 0 12 12"><circle cx="6" cy="6" r="5.5" fill="#1f6f9e"/></svg>
      brightpathacademy
    </p>
  </div>
</section>

</body>
</html>
```